Holvern Incorporated

Holvern is a business that provides consulting, and manages and supplies trades persons in the construction and heavy industries sector. We build, do maintenance, install machinery, and can manage projects or jobs. Would like or prefer more clean, classic designs. Blacks/greys, but open to almost anything.

Target Market(s)

Industrial/Construction/Manufacturing

Industry/Entity Type

Construction Company

Contact Information for Business Card

Clean, business name on the front, possibly have the details on the back, but open to any ideas.

Logo Text

We currently do not have a slogan, open to ideas

Font styles to use
Serif
Sans Serif

Colors

Designer to choose colors to be used in the design.

Requirements
Should not have
• the oval is not my logo, was just an idea. please don't send 20 designs with the oval

```html
<!DOCTYPE html>
<html lang="en">
<head>
<meta charset="UTF-8">
<title>Holvern Incorporated – Business Card</title>
<link rel="stylesheet" href="https://fonts.googleapis.com/css2?family=Roboto+Slab:wght@500&family=Roboto:wght@400;700&display=swap">
<style>
  :root {
    --canvas: #3a3a3a;
    --ink: #0b0b0b;
    --paper: #ffffff;
    --grey: #8a8a8a;
    --text: #1a1a1a;
    --muted: #333333;
  }
  * { box-sizing: border-box; margin: 0; padding: 0; }
  html, body { width: 1200px; height: 800px; overflow: hidden; }
  body { background: var(--canvas); position: relative; font-family: "Roboto", Arial, sans-serif; }

  .card {
    position: absolute;
    width: 620px;
    height: 354px;
    box-shadow: 0 10px 28px rgba(0,0,0,.45);
    overflow: hidden;
  }

  /* Front */
  .card--front { left: 150px; top: 40px; background: var(--ink); }
  .card--front .brand { position: absolute; left: 0; right: 0; top: 118px; text-align: center; color: var(--paper); }

  .brand-name {
    font-family: "Roboto Slab", Georgia, serif;
    font-weight: 500;
    line-height: 1;
  }
  .card--front .brand-name { font-size: 84px; }
  .brand-suffix {
    font-family: "Roboto Slab", Georgia, serif;
    font-weight: 500;
    letter-spacing: .18em;
    display: block;
    margin-top: 10px;
  }
  .card--front .brand-suffix { font-size: 12px; }

  /* Back */
  .card--back { left: 430px; top: 400px; background: var(--paper); }
  .card--back .swoosh { position: absolute; inset: 0; }
  .card--back .brand { position: absolute; left: 44px; top: 118px; width: 250px; text-align: center; color: var(--ink); }
  .card--back .brand-name { font-size: 54px; }
  .card--back .brand-suffix { font-size: 9px; margin-top: 6px; }

  .divider { position: absolute; left: 318px; top: 58px; width: 1.5px; height: 138px; background: var(--text); }

  .details { position: absolute; left: 342px; top: 46px; color: var(--text); }
  .person-name { font-weight: 700; font-size: 20px; }
  .person-role { font-size: 15px; color: var(--muted); margin-top: 2px; margin-left: 8px; }
  .address { font-size: 15px; color: var(--muted); margin-top: 10px; margin-left: 8px; line-height: 1.2; }
  .contacts { list-style: none; margin-top: 10px; margin-left: 12px; }
  .contacts li { display: flex; align-items: center; gap: 10px; font-size: 15px; color: var(--muted); line-height: 1.45; }
  .contacts svg { width: 13px; height: 13px; fill: #555; flex: none; }
</style>
</head>
<body>

  <section class="card card--front" aria-label="Card front">
    <div class="brand">
      <span class="brand-name">Holvern</span>
      <span class="brand-suffix">INCORPORATED</span>
    </div>
  </section>

  <section class="card card--back" aria-label="Card back">
    <svg class="swoosh" viewBox="0 0 620 354" preserveAspectRatio="none" aria-hidden="true">
      <path d="M0,322 C260,318 480,292 620,196 L620,214 C480,310 260,334 0,336 Z" fill="var(--grey)"/>
      <path d="M110,354 C340,346 520,318 620,232 L620,354 Z" fill="var(--ink)"/>
    </svg>

    <div class="brand">
      <span class="brand-name">Holvern</span>
      <span class="brand-suffix">INCORPORATED</span>
    </div>

    <div class="divider"></div>

    <div class="details">
      <p class="person-name">Darren Kessler</p>
      <p class="person-role">Manager</p>
      <p class="address">Your address, city<br>state, ZIP 0000</p>
      <ul class="contacts">
        <li>
          <svg viewBox="0 0 24 24"><path d="M6.6 10.8a15.1 15.1 0 0 0 6.6 6.6l2.2-2.2c.3-.3.7-.4 1-.2 1.1.4 2.3.6 3.6.6.6 0 1 .4 1 1V20c0 .6-.4 1-1 1A17 17 0 0 1 3 4c0-.6.4-1 1-1h3.5c.6 0 1 .4 1 1 0 1.2.2 2.4.6 3.6.1.3 0 .7-.2 1z"/></svg>
          555-014-2100
        </li>
        <li>
          <svg viewBox="0 0 24 24"><path d="M2 5h20v14H2z M4 7v.3l8 5.2 8-5.2V7z" fill-rule="evenodd"/></svg>
          contact@holvernco.com
        </li>
        <li>
          <svg viewBox="0 0 24 24"><path d="M12 2a10 10 0 1 0 0 20 10 10 0 0 0 0-20zm0 5a5 5 0 1 1 0 10 5 5 0 0 1 0-10z" fill-rule="evenodd"/></svg>
          www.holvernco.com
        </li>
      </ul>
    </div>
  </section>

</body>
</html>
```